Emergency and Referral Vet Hospital promotional sticker design

We're looking at getting some stickers designed that we could give to clients to put on their cars for promotion and advertising. If they could also be suitable for a goodie bag for conference too that would be great. I like the look of water-colour backgrounds, we'll need to include our logo and probably our address (Unit 4/372 Tarvenny Drive Success). We also have a hospital motto "... because they're family" if that could somehow be integrated, we only care for small animals (dogs, cats etc) but the design is very open to suggestion. Would love to see what you can create.

Industry/Entity Type

Veterinary

Colors
0054AA
0677BA
7BADD7
CADEEF
E8F1F8
0094D4
00A9DD
6FCCEA
C7EBF8
E9F6FB

Requirements
Nice to have
• Think beach vibes, blues maybe paw print shapes etc

```html
<!DOCTYPE html>
<html lang="en">
<head>
<meta charset="utf-8">
<title>tides – because they're family stickers</title>
<link rel="stylesheet" href="https://fonts.googleapis.com/css2?family=Kaushan+Script&family=Outfit:wght@600;700&display=swap">
<style>
  :root {
    --page: #ffffff;
    --ink: #0b0b0b;
    --navy: #0d4a6e;
    --aqua: #33d3ea;
    --sky: #8fd9f2;
    --lilac: #b9c6fb;
    --mist: #e9f6fb;
    --slate: #7ba3cc;
    --ice: #cadeef;
    --frost: #e8f1f8;
  }
  * { margin: 0; padding: 0; box-sizing: border-box; }
  html, body { width: 1000px; height: 1200px; overflow: hidden; background: var(--page); }
  .canvas { position: relative; width: 1000px; height: 1200px; }

  .sticker { position: absolute; }
  .tagline {
    position: absolute;
    font-family: "Kaushan Script", cursive;
    color: var(--navy);
    white-space: nowrap;
    line-height: 1;
  }
  .brand-mark {
    position: absolute;
    border-radius: 50%;
    background: var(--navy);
  }
  .brand-name {
    position: absolute;
    font-family: "Outfit", sans-serif;
    font-weight: 700;
    color: var(--ink);
    text-align: center;
    line-height: 1;
    letter-spacing: 0.5px;
  }
  .address {
    position: absolute;
    font-family: "Outfit", sans-serif;
    font-weight: 600;
    color: var(--ink);
    text-align: center;
    line-height: 1.3;
    white-space: nowrap;
  }

  /* Round watercolour sticker */
  .sticker--splash { left: 0; top: 0; width: 1000px; height: 600px; }
  .splash-wash {
    position: absolute;
    left: 215px; top: 80px; width: 575px; height: 465px;
    border-radius: 48% 52% 44% 56% / 55% 45% 58% 42%;
    background:
      radial-gradient(ellipse at 38% 48%, var(--aqua) 0%, rgba(51,211,234,0.55) 30%, transparent 62%),
      radial-gradient(ellipse at 72% 40%, var(--lilac) 0%, transparent 55%),
      radial-gradient(ellipse at 50% 50%, var(--sky) 0%, var(--mist) 65%, rgba(255,255,255,0) 78%);
    filter: blur(4px);
  }
  .sticker--splash .tagline { left: 336px; top: 258px; font-size: 37px; }
  .sticker--splash .brand-mark { left: 482px; top: 322px; width: 64px; height: 64px; }
  .sticker--splash .brand-name { left: 413px; top: 422px; width: 200px; font-size: 40px; }
  .sticker--splash .address { left: 413px; top: 461px; width: 200px; font-size: 14px; }

  /* Square agate sticker */
  .sticker--square { left: 292px; top: 637px; width: 424px; height: 423px; overflow: hidden; }
  .agate-wash {
    position: absolute; inset: 0;
    background:
      linear-gradient(135deg, var(--slate) 0%, var(--ice) 28%, var(--frost) 48%, transparent 64%),
      linear-gradient(20deg, var(--ice) 0%, var(--frost) 30%, transparent 48%),
      var(--page);
  }
  .sticker--square .tagline { left: 21px; top: 106px; font-size: 40px; }
  .sticker--square .brand-mark { left: 270px; top: 238px; width: 70px; height: 70px; }
  .sticker--square .brand-name { left: 205px; top: 329px; width: 200px; font-size: 38px; }
  .sticker--square .address { left: 185px; top: 374px; width: 240px; font-size: 16px; }
</style>
</head>
<body>
<main class="canvas">

  <section class="sticker sticker--splash">
    <div class="splash-wash" role="img" aria-label="Soft aqua and lilac watercolour splash with white paw prints and a medical cross outline"></div>
    <p class="tagline">… because they're family</p>
    <span class="brand-mark" aria-hidden="true"></span>
    <p class="brand-name">tides</p>
    <p class="address">Unit 4<br>372 Tarvenny Drive Success</p>
  </section>

  <section class="sticker sticker--square">
    <div class="agate-wash" role="img" aria-label="Blue watercolour agate wave bands with white paw prints"></div>
    <p class="tagline">… because they're family</p>
    <span class="brand-mark" aria-hidden="true"></span>
    <p class="brand-name">tides</p>
    <p class="address">Unit 4<br>372 Tarvenny Drive Success</p>
  </section>

</main>
</body>
</html>
```